Qamra
قمرة كافيه
Hello Designers:-
Please check your e-mail inbox.
Thank you so much!
plz star rating...
The front and the back of the card should be one color "Beige". In front, it only shows the logo, the address, e-mail, twitter and instagram accounts. No need to type any other word like the word "قمرة"
As for the back, we want a loyalty card with 6 stamps with "Qamra" shape drawing on each. and the 6th qamra has a FREE written on it (Pic provided in brief)
If you have any comments, questions or requirements please do not hesitate to contact me on my e-mail or here, in the discussion.
Thank you so much for your work! :)
Hello designers: Please make sure to read the project brief as we want a (Double) sided business card/loyalty card. Moreover, please be aware that the card color should follow the color of the store "Beige" and not the logo color (Store pic provided in the brief)
Thank you so much for your effort! And good luck!

```html
<!DOCTYPE html>
<html lang="en">
<head>
<meta charset="utf-8">
<title>Qamra – Business &amp; Loyalty Card</title>
<link rel="stylesheet" href="https://fonts.googleapis.com/css2?family=Open+Sans:wght@400;600&family=Archivo+Black&family=Noto+Sans+Arabic:wght@400&display=swap">
<style>
  :root {
    --backdrop: #e4e2df;
    --card-beige: #d3b689;
    --ink: #3b2f23;
    --stamp: #e6e4e1;
    --stamp-art-light: #fbfaf8;
    --stamp-art-edge: #eeece9;
    --logo-white: #fbf8f2;
    --free-black: #111111;
  }
  * { box-sizing: border-box; margin: 0; padding: 0; }
  html, body {
    width: 1200px; height: 852px; overflow: hidden;
    background: var(--backdrop);
  }
  .canvas {
    position: relative; width: 1200px; height: 852px;
    display: flex; align-items: center; justify-content: center; gap: 60px;
  }
  .card {
    position: relative; width: 530px; height: 318px;
    background: var(--card-beige); border-radius: 18px;
    box-shadow: 0 6px 18px rgba(0,0,0,0.18);
    overflow: hidden;
  }

  /* Front */
  .brand {
    position: absolute; left: 232px; top: 62px;
    display: flex; align-items: center; gap: 12px;
  }
  .brand-mark {
    width: 14px; height: 14px; border-radius: 50%;
    background: var(--logo-white); flex: none;
  }
  .brand-name {
    font-family: "Open Sans", sans-serif; font-weight: 600;
    font-size: 46px; line-height: 1; color: var(--logo-white);
  }
  .contact {
    position: absolute; left: 30px; top: 190px;
    font-family: "Open Sans", sans-serif; font-size: 13px; color: var(--ink);
  }
  .contact-address {
    font-family: "Noto Sans Arabic", sans-serif; font-size: 13px; line-height: 18px;
    direction: rtl; text-align: left; margin-bottom: 10px;
  }
  .contact-list { list-style: none; }
  .contact-item { display: flex; align-items: center; gap: 9px; height: 19px; line-height: 19px; }
  .contact-icon { width: 12px; height: 12px; flex: none; }
  .dot { width: 11px; height: 11px; border-radius: 50%; background: var(--ink); flex: none; }

  /* Back */
  .stamps {
    position: absolute; left: 58px; top: 34px;
    display: grid; grid-template-columns: repeat(3, 106px);
    column-gap: 46px; row-gap: 34px;
  }
  .stamp {
    position: relative; width: 106px; height: 106px; border-radius: 50%;
    background: var(--stamp);
  }
  .stamp-art {
    position: absolute; left: 24px; top: 14px; width: 58px; height: 78px;
    border-radius: 40% 40% 30% 30%;
    background: radial-gradient(ellipse at 50% 45%, var(--stamp-art-light) 0%, var(--stamp-art-edge) 100%);
  }
  .stamp-free {
    position: absolute; right: -20px; bottom: -18px;
    font-family: "Archivo Black", sans-serif; font-size: 26px; line-height: 1;
    color: var(--free-black); transform: rotate(-6deg);
  }
</style>
</head>
<body>
<main class="canvas">
  <section class="card card-front" aria-label="Card front">
    <div class="brand">
      <span class="brand-mark"></span>
      <span class="brand-name">Qamra</span>
    </div>
    <div class="contact">
      <p class="contact-address">الكويت - السالمية، شارع البحر</p>
      <ul class="contact-list">
        <li class="contact-item">
          <svg class="contact-icon" viewBox="0 0 24 24"><path fill="#3b2f23" d="M6.6 10.8a15 15 0 0 0 6.6 6.6l2.2-2.2c.3-.3.7-.4 1-.2 1.1.4 2.3.6 3.6.6.6 0 1 .4 1 1V20c0 .6-.4 1-1 1A17 17 0 0 1 3 4c0-.6.4-1 1-1h3.5c.6 0 1 .4 1 1 0 1.3.2 2.5.6 3.6.1.3 0 .7-.2 1z"/></svg>
          <span>96612047</span>
        </li>
        <li class="contact-item">
          <svg class="contact-icon" viewBox="0 0 24 24"><rect x="2" y="5" width="20" height="14" rx="1.5" fill="#3b2f23"/><path d="M3 6l9 7 9-7" fill="none" stroke="#d3b689" stroke-width="1.8"/></svg>
          <span>QamraKuwait@qamramail.com</span>
        </li>
        <li class="contact-item"><span class="dot"></span><span>@Qamra</span></li>
        <li class="contact-item"><span class="dot"></span><span>@QamraKuwait</span></li>
      </ul>
    </div>
  </section>

  <section class="card card-back" aria-label="Card back, loyalty stamps">
    <div class="stamps">
      <div class="stamp"><div class="stamp-art" role="img" aria-label="White coffee pot drawing"></div></div>
      <div class="stamp"><div class="stamp-art" role="img" aria-label="White coffee pot drawing"></div></div>
      <div class="stamp"><div class="stamp-art" role="img" aria-label="White coffee pot drawing"></div></div>
      <div class="stamp"><div class="stamp-art" role="img" aria-label="White coffee pot drawing"></div></div>
      <div class="stamp"><div class="stamp-art" role="img" aria-label="White coffee pot drawing"></div></div>
      <div class="stamp">
        <div class="stamp-art" role="img" aria-label="White coffee pot drawing"></div>
        <span class="stamp-free">FREE</span>
      </div>
    </div>
  </section>
</main>
</body>
</html>
```